Emerging Ed-Tech Startup seeking Stationery Designs!

We are in need of basic set of stationery designs to be used for our business operations, letters, emails, and in-office materials. We are a technology startup enhancing on campus work experience offerings by establishing a collaborative work environment for the completion of such tasks.

Our colors are Vibrant Tiffany Blue/Black/White.

Website: www.campusmeridian.com (Still under construction aside from the landing pages)

Please make sure the designs use a brighter more vibrant tiffany blue color than seen in the image files uploaded. We are not using those materials.

Our logo has been added as a file as well, please use that for any designs (include that logo). Thank you.

```html
<!DOCTYPE html>
<html lang="en">
<head>
<meta charset="utf-8">
<title>Campus Meridian — Stationery Set</title>
<link rel="stylesheet" href="https://fonts.googleapis.com/css2?family=Jost:wght@400;500;600;700&display=swap">
<style>
  :root {
    --aqua: #0be3e6;
    --ink: #111111;
    --paper: #ffffff;
    --backdrop: #e8e5e0;
    --rule: #3a3a3a;
    --ghost: #eef1f2;
    --ghost-ink: #cfd6d8;
    --text: #222222;
  }
  * { box-sizing: border-box; margin: 0; padding: 0; }
  html, body { width: 1200px; height: 706px; overflow: hidden; }
  body {
    position: relative;
    background: var(--backdrop);
    font-family: "Jost", sans-serif;
    color: var(--text);
  }
  .sheet {
    position: absolute;
    background: var(--paper);
    border: 1px solid #9a9a9a;
    overflow: hidden;
  }
  .brand {
    position: absolute;
    display: flex;
    align-items: center;
    gap: 4px;
  }
  .brand-square { width: 9px; height: 9px; background: var(--aqua); flex: none; }
  .brand-name {
    font-weight: 700;
    color: var(--ink);
    text-transform: uppercase;
    line-height: 0.95;
    font-size: 12px;
    letter-spacing: 0.2px;
  }
  .contact-list { position: absolute; list-style: none; font-size: 6.3px; line-height: 7.6px; color: var(--text); }
  .contact-list li, .contact-row span { display: flex; align-items: center; gap: 3px; white-space: nowrap; }
  .icon { width: 5px; height: 5px; fill: var(--aqua); flex: none; }
  .icon-dark { fill: var(--ink); }
  .band { position: absolute; left: 0; bottom: 0; width: 100%; display: block; }
  .band-dark { fill: var(--ink); }
  .band-aqua { fill: var(--aqua); }
  .address { position: absolute; font-size: 6.3px; letter-spacing: 0.3px; display: flex; align-items: center; gap: 3px; white-space: nowrap; }
  .ghost-mark {
    position: absolute;
    background: var(--ghost);
    color: var(--ghost-ink);
    font-weight: 700;
    text-transform: uppercase;
    display: flex;
    align-items: center;
    justify-content: center;
    text-align: center;
    line-height: 1;
  }

  /* Letterhead */
  .letterhead { left: 61px; top: 45px; width: 334px; height: 430px; }
  .letterhead .brand { left: 24px; top: 18px; }
  .letterhead .contact-list { left: 223px; top: 20px; }
  .letterhead .ghost-mark { left: 92px; top: 150px; width: 155px; height: 150px; font-size: 26px; }
  .letterhead .address { left: 0; right: 0; justify-content: center; top: 403px; }
  .letterhead .band { height: 13px; }

  /* Fax */
  .fax { left: 422px; top: 46px; width: 333px; height: 430px; }
  .fax .brand { left: 30px; top: 18px; }
  .fax .header-address { position: absolute; left: 241px; top: 32px; padding-left: 4px; border-left: 1px solid var(--rule); font-size: 6px; line-height: 14px; }
  .fax-title { position: absolute; left: 28px; top: 94px; font-size: 20px; font-weight: 400; letter-spacing: 0.5px; color: var(--ink); }
  .fax-fields { position: absolute; left: 31px; top: 136px; width: 271px; display: grid; grid-template-columns: 160px 96px; column-gap: 15px; row-gap: 25px; }
  .fax-field { font-size: 7.5px; border-bottom: 1px solid var(--rule); height: 13px; }
  .contact-row { position: absolute; left: 24px; top: 404px; display: flex; gap: 7px; font-size: 5.8px; }
  .fax .band { height: 13px; }

  /* Envelopes */
  .envelope { width: 363px; height: 156px; }
  .envelope .flap { position: absolute; left: 0; top: 0; width: 100%; height: 55px; display: flex; align-items: center; justify-content: center; }
  .envelope .brand-name { font-size: 11px; }
  .envelope .brand { position: static; }
  .envelope-white { left: 775px; top: 48px; }
  .envelope-white .flap { border-bottom: 1px solid #8a8a8a; }
  .envelope-black { left: 781px; top: 151px; height: 157px; }
  .envelope-black .flap { background: var(--ink); }
  .envelope-black .brand-name { color: var(--paper); }
  .envelope-black .brand-square { background: var(--paper); }
  .envelope-aqua { left: 777px; top: 313px; width: 361px; height: 157px; }
  .envelope-aqua .flap { background: var(--aqua); }
  .envelope-aqua .brand-name { color: var(--paper); }
  .envelope-aqua .brand-square { background: var(--paper); }

  /* Business card */
  .business-card { left: 104px; top: 519px; width: 354px; height: 104px; }
  .business-card .brand { left: 16px; top: 14px; }
  .business-card .brand-name { font-size: 10.5px; }
  .card-holder { position: absolute; right: 18px; top: 19px; text-align: right; }
  .card-holder .name { font-size: 8px; font-weight: 600; letter-spacing: 0.6px; color: var(--ink); }
  .card-holder .role { font-size: 6.5px; letter-spacing: 0.2px; margin-top: 1px; }
  .business-card .contact-list { left: 16px; top: 55px; font-size: 6px; line-height: 8.5px; }
  .business-card .address { right: 18px; top: 77px; }
  .business-card .band { height: 13px; }

  /* Compliment slip */
  .compliment-slip { left: 544px; top: 502px; width: 373px; height: 166px; }
  .compliment-slip .brand { left: 20px; top: 16px; }
  .compliment-slip .address { left: 19px; top: 66px; }
  .compliment-slip .web { position: absolute; left: 19px; top: 141px; font-size: 6.3px; letter-spacing: 0.3px; }
  .compliment-slip .ghost-mark { left: 316px; top: 106px; width: 42px; height: 38px; font-size: 7px; }
  .compliment-slip .band { height: 13px; }
</style>
</head>
<body>

<svg width="0" height="0" style="position:absolute" aria-hidden="true">
  <symbol id="i-phone" viewBox="0 0 10 10"><path d="M2 0.5h2l1 2.5-1.3 1a5.5 5.5 0 0 0 2.3 2.3l1-1.3 2.5 1v2a1 1 0 0 1-1 1A8.5 8.5 0 0 1 1 1.5a1 1 0 0 1 1-1z"/></symbol>
  <symbol id="i-mobile" viewBox="0 0 10 10"><rect x="2.5" y="0" width="5" height="10" rx="1"/></symbol>
  <symbol id="i-mail" viewBox="0 0 10 10"><path d="M0 2h10v6H0z M0 2l5 3.5L10 2"/></symbol>
  <symbol id="i-web" viewBox="0 0 10 10"><circle cx="5" cy="5" r="5"/></symbol>
  <symbol id="i-home" viewBox="0 0 10 10"><path d="M5 0.5L0 5h1.5v4.5h2.5v-3h2v3h2.5V5H10z"/></symbol>
  <symbol id="i-band" viewBox="0 0 100 10"><polygon class="band-dark" points="0,0 52,0 48.5,10 0,10"/><polygon class="band-aqua" points="54,0 100,0 100,10 50.5,10"/></symbol>
</svg>

<!-- Letterhead -->
<section class="sheet letterhead">
  <div class="brand"><span class="brand-square"></span><span class="brand-name">Campus<br>Meridian</span></div>
  <ul class="contact-list">
    <li><svg class="icon"><use href="#i-phone"/></svg>(555) 201-4470</li>
    <li><svg class="icon"><use href="#i-mobile"/></svg>(555) 318-2094</li>
    <li><svg class="icon"><use href="#i-mail"/></svg>Marcus@CampusMeridian.com</li>
    <li><svg class="icon"><use href="#i-web"/></svg>www.campusmeridian.com</li>
  </ul>
  <div class="ghost-mark" role="img" aria-label="Faint brand watermark">Campus<br>Meridian</div>
  <p class="address"><svg class="icon icon-dark"><use href="#i-home"/></svg>Suite B-14 Harbor Lane</p>
  <svg class="band" viewBox="0 0 100 10" preserveAspectRatio="none"><use href="#i-band"/></svg>
</section>

<!-- Fax cover -->
<section class="sheet fax">
  <div class="brand"><span class="brand-square"></span><span class="brand-name">Campus<br>Meridian</span></div>
  <p class="header-address">Suite B-14 Harbor Lane</p>
  <h1 class="fax-title">FAX</h1>
  <div class="fax-fields">
    <div class="fax-field">To</div><div class="fax-field">From</div>
    <div class="fax-field">Fax</div><div class="fax-field">Pages</div>
    <div class="fax-field">Phone</div><div class="fax-field">Date</div>
    <div class="fax-field">Re</div><div class="fax-field">CC</div>
  </div>
  <div class="contact-row">
    <span><svg class="icon"><use href="#i-phone"/></svg>(555) 201-4470</span>
    <span><svg class="icon"><use href="#i-mobile"/></svg>(555) 318-2094</span>
    <span><svg class="icon"><use href="#i-mail"/></svg>Marcus@CampusMeridian.com</span>
    <span><svg class="icon"><use href="#i-web"/></svg>www.campusmeridian.com</span>
  </div>
  <svg class="band" viewBox="0 0 100 10" preserveAspectRatio="none"><use href="#i-band"/></svg>
</section>

<!-- Envelopes -->
<section class="sheet envelope envelope-white">
  <div class="flap"><div class="brand"><span class="brand-square"></span><span class="brand-name">Campus<br>Meridian</span></div></div>
</section>
<section class="sheet envelope envelope-black">
  <div class="flap"><div class="brand"><span class="brand-square"></span><span class="brand-name">Campus<br>Meridian</span></div></div>
</section>
<section class="sheet envelope envelope-aqua">
  <div class="flap"><div class="brand"><span class="brand-square"></span><span class="brand-name">Campus<br>Meridian</span></div></div>
</section>

<!-- Business card -->
<section class="sheet business-card">
  <div class="brand"><span class="brand-square"></span><span class="brand-name">Campus<br>Meridian</span></div>
  <div class="card-holder">
    <p class="name">MARCUS ELLERY</p>
    <p class="role">Chief Executive Officer</p>
  </div>
  <ul class="contact-list">
    <li><svg class="icon"><use href="#i-phone"/></svg>(555) 201-4470</li>
    <li><svg class="icon"><use href="#i-mobile"/></svg>(555) 318-2094</li>
    <li><svg class="icon"><use href="#i-mail"/></svg>Marcus@CampusMeridian.com</li>
    <li><svg class="icon"><use href="#i-web"/></svg>www.campusmeridian.com</li>
  </ul>
  <p class="address">Suite B-14 Harbor Lane</p>
  <svg class="band" viewBox="0 0 100 10" preserveAspectRatio="none"><use href="#i-band"/></svg>
</section>

<!-- Compliment slip -->
<section class="sheet compliment-slip">
  <div class="brand"><span class="brand-square"></span><span class="brand-name">Campus<br>Meridian</span></div>
  <p class="address">Suite B-14 Harbor Lane</p>
  <p class="web">www.campusmeridian.com</p>
  <div class="ghost-mark" role="img" aria-label="Faint brand watermark">Campus<br>Meridian</div>
  <svg class="band" viewBox="0 0 100 10" preserveAspectRatio="none"><use href="#i-band"/></svg>
</section>

</body>
</html>
```